Flyer for Leaflet Dropping - A5 - Managed IT Support Flyer

I need an A5 double sided flyer LANDSCAPE - design for door to door leaflet dropping / marketing to local businesses.
Our main aim is to promote our ‘Managed IT Support’ services to local small and medium businesses.
Our secondary aim is to promote our additional services which are internet/communications and cloud services. We want to mention these services but they are only secondary therefore need to take a smaller focus and not detract from the main message of the flyer.
• Hosted Cloud Desktop
• VOIP Telephone Systems
• Desk Suite
• Cloud Services
• Internet Services
• Disaster Recovery

Target Market(s)

Our target audience is senior members of company (MD, FD, Owners, Operations, Management), looking to outsource their IT requirements/needs. UK Only. N London

Industry/Entity Type

Information Technology

Font styles to use
Sans Serif

Requirements
Must have
• Please use the website for a source of information and inspiration – www.brantolhub.co.uk.
• We specifically feel the points below are important and want to see them feature.
• 1. Large bold heading highlighting our primary service ‘Managed IT Support’
• 2. Secondary sub-heading explaining exactly what we do.
• ‘We manage your IT ensuring systems are monitored, supported and protected to enhance business growth.’
• 3. Reasons to choose BrantolHub – take inspiration from https://www.brantolhub.co.uk/about-us/
• 4. No Risk - Our 90 Day Satisfaction Guarantee (see website).
• 5. Areas we cover: ‘Trusted by 100+ businesses across Hertfordshire, Essex, London & beyond.‘
• 6. Name of company, contact details.
• CALL TO ACTION
• 1. Call Us – 03337159264
• 2. Visit our Website – https://www.brantolhub.co.uk/gomanaged

```html
<!DOCTYPE html>
<html lang="en">
<head>
<meta charset="utf-8">
<title>BrantolHub – Managed IT Support Flyer</title>
<link rel="stylesheet" href="https://fonts.googleapis.com/css2?family=Oswald:wght@500;600&family=Mulish:wght@400;600&family=Noto+Sans:wght@400;700&display=swap">
<style>
  :root{
    --stage:#bcbdc0;
    --blue:#3b9ad8;
    --blue-deep:#2a86c8;
    --charcoal:#4a4a4d;
    --grey:#8a8a8c;
    --pale:#e6e7e8;
    --green:#7cc04b;
    --purple:#9b6bb5;
    --red:#ef5a5f;
    --ink:#333;
    --white:#fff;
  }
  html,body{margin:0;padding:0}
  body{width:914px;height:1200px;overflow:hidden;background:var(--stage);position:relative;font-family:"Mulish",sans-serif}
  .flyer{position:absolute;left:104px;width:882px;height:621px;background:var(--white);overflow:hidden;transform:scale(.8);transform-origin:0 0}
  .flyer--front{top:92px}
  .flyer--back{top:642px}
  .shapes{position:absolute;left:0;top:0;width:882px;height:621px}
  .abs{position:absolute;margin:0}
  .brand{left:45px;top:28px;display:flex;align-items:center;gap:12px}
  .brand__mark{width:52px;height:52px;border-radius:50%;background:var(--blue)}
  .brand__name{font-family:"Mulish",sans-serif;font-weight:600;font-size:38px;color:var(--charcoal);line-height:1}
  .brand__tag{font-size:13px;color:var(--grey);letter-spacing:.5px;margin-top:2px}
  .headline{font-family:"Oswald",sans-serif;font-weight:600;color:var(--white);font-size:56px;line-height:1;left:432px;top:26px;letter-spacing:-.5px;white-space:nowrap;transform:scaleX(.9);transform-origin:0 0}
  .headline--spaced{font-size:44px;letter-spacing:4px;left:445px;top:44px;font-weight:500;transform:scaleX(.92)}
  .intro{left:442px;top:116px;color:var(--white);font-size:20.5px;line-height:27px}
  .intro span{display:block}
  .coverage{left:443px;top:210px;width:441px;height:60px;background:var(--charcoal);color:var(--white);font-size:16px;line-height:22px;padding:7px 0 0 26px;box-sizing:border-box}
  .feature{color:var(--white);font-family:"Noto Sans",sans-serif;text-align:center;font-size:12.5px;line-height:15.5px}
  .feature h3{font-size:18px;font-weight:700;margin:0 0 4px}
  .feature b{font-weight:700}
  .cta{left:118px;top:488px;font-size:29px;color:var(--grey);display:flex;align-items:center;gap:8px;letter-spacing:.3px}
  .cta strong{color:var(--ink);font-weight:400}
  .address{left:126px;top:528px;font-size:16px;line-height:21px;color:var(--ink)}
  .web{left:134px;top:594px;font-size:16px;color:var(--white);letter-spacing:2.6px}
  .risk__title{left:577px;top:499px;font-family:"Noto Sans",sans-serif;font-weight:700;font-size:28px;color:var(--white);line-height:1}
  .risk__text{left:578px;top:530px;font-family:"Noto Sans",sans-serif;font-weight:700;font-size:17px;line-height:19px;color:var(--ink);text-align:center}
  .caption{left:58px;top:385px;color:var(--white);font-size:17px;line-height:22px}
  .service{color:var(--white)}
  .service h3{font-weight:400;font-size:24px;margin:0;line-height:28px}
  .service p{font-size:16px;line-height:21px;margin:0 0 0 6px}
</style>
</head>
<body>

<section class="flyer flyer--front">
  <svg class="shapes" viewBox="0 0 882 621">
    <defs>
      <linearGradient id="officeTone" x1="0" y1="0" x2="1" y2="1">
        <stop offset="0" stop-color="#d8d4cf"/><stop offset=".5" stop-color="#b9b3ad"/><stop offset="1" stop-color="#8d96a3"/>
      </linearGradient>
    </defs>
    <polygon points="323,0 882,0 882,380 430,380" fill="var(--blue)"/>
    <polygon points="0,110 360,110 440,378 0,378" fill="url(#officeTone)" role="img" aria-label="Photo of a smiling support agent with a headset in a bright office"/>
    <line x1="388" y1="22" x2="423" y2="105" stroke="#fff" stroke-width="1.2"/>
    <circle cx="388" cy="22" r="4" fill="#fff"/>
    <line x1="423" y1="105" x2="882" y2="105" stroke="#fff" stroke-width="1.2"/>
    <polygon points="0,455 85,585 500,585 530,621 0,621" fill="var(--grey)"/>
    <polygon points="45,318 290,318 350,463 80,463" fill="var(--green)"/>
    <polygon points="285,318 525,318 588,463 348,463" fill="var(--purple)"/>
    <polygon points="525,318 775,318 832,463 588,463" fill="var(--red)"/>
    <circle cx="183" cy="318" r="36" fill="var(--green)"/>
    <circle cx="410" cy="318" r="36" fill="var(--purple)"/>
    <circle cx="652" cy="318" r="36" fill="var(--red)"/>
    <g fill="none" stroke="#fff" stroke-width="3.5" stroke-linecap="round">
      <path d="M166,303 A21,21 0 1 1 164,330"/>
      <polyline points="160,296 166,303 174,298"/>
      <polyline points="184,306 184,320 194,326"/>
    </g>
    <polygon points="410,294 417,309 433,311 421,322 424,338 410,330 396,338 399,322 387,311 403,309" fill="none" stroke="#fff" stroke-width="2.5" stroke-linejoin="round"/>
    <g fill="none" stroke="#fff" stroke-width="2.5" stroke-linejoin="round">
      <rect x="632" y="315" width="9" height="22"/>
      <path d="M641,317 L651,303 L652,294 Q658,293 659,302 L657,312 L671,312 Q676,313 674,319 L671,335 Q669,338 664,338 L641,338"/>
    </g>
    <polygon points="520,488 882,488 882,598 560,598" fill="var(--pale)"/>
    <polygon points="520,503 735,503 735,528 532,528" fill="var(--blue)"/>
    <g transform="translate(792,545)">
      <path d="M0,-64 l8,5 9,-3 5,8 9,1 1,9 8,5 -2,9 6,7 -5,8 3,9 -8,5 0,9 -9,3 -3,9 -9,0 -5,8 -9,-3 -8,5 -6,-7 -9,0 -2,-9 -8,-5 2,-9 -5,-8 5,-7 -2,-9 8,-5 1,-9 9,-1 4,-8 9,3 z" transform="scale(1.05)" fill="var(--blue)"/>
      <circle r="52" fill="var(--blue)"/>
      <circle r="46" fill="none" stroke="#fff" stroke-width="2"/>
      <circle r="26" fill="none" stroke="#fff" stroke-width="2"/>
      <text y="10" text-anchor="middle" font-family="Oswald,sans-serif" font-weight="600" font-size="26" fill="#fff">100%</text>
      <text y="-32" text-anchor="middle" font-family="Noto Sans,sans-serif" font-weight="700" font-size="8.5" fill="#fff" letter-spacing=".5">SATISFACTION</text>
      <text y="39" text-anchor="middle" font-family="Noto Sans,sans-serif" font-weight="700" font-size="8.5" fill="#fff" letter-spacing=".5">GUARANTEED</text>
    </g>
    <g transform="translate(243,495)" fill="var(--blue-deep)">
      <path d="M2,10 Q12,0 22,10 L19,13 Q12,8 5,13 Z"/>
      <rect x="5" y="13" width="14" height="10" rx="2"/>
    </g>
  </svg>

  <div class="abs brand">
    <span class="brand__mark"></span>
    <div><div class="brand__name">BrantolHub</div><div class="brand__tag">Helping you work smarter</div></div>
  </div>

  <h1 class="abs headline">Managed IT Support</h1>
  <p class="abs intro"><span>We manage your IT ensuring systems</span><span style="padding-left:12px">are monitored, supported and protected</span><span style="padding-left:18px">to enhance business growth.</span></p>
  <p class="abs coverage">Trusted by 100+ businesses across Hertfordshire,<br>Essex, London &amp; beyond</p>

  <div class="abs feature" style="left:88px;top:356px;width:220px">
    <h3>Fast Response Times</h3>
    <b>Super fast</b> service desk with an industry leading average wait time of <b>under 13 seconds</b>
  </div>
  <div class="abs feature" style="left:330px;top:356px;width:224px">
    <h3>Fully Accredited</h3>
    Northvale <b>Gold</b> Partner, Tier-1 CSP Partner, TechCert Managed Services and VoxLine <b>Platinum Partner</b>
  </div>
  <div class="abs feature" style="left:578px;top:356px;width:220px">
    <h3>Years of Experince</h3>
    We've been in business for <b>over 10 years</b> and now support over <b>100+ customers</b>
  </div>

  <div class="abs cta">CALL US <span style="width:28px"></span><strong>03337159264</strong></div>
  <p class="abs address">BrantolHub Ltd, Unit 5, Ravensby Court,<br>&nbsp;Hertford, Hertfordshire, SG13 4PX</p>
  <p class="abs web">www.brantolhub.co.uk/gomanaged</p>

  <p class="abs risk__title">NO RISK</p>
  <p class="abs risk__text">OUR 90 DAY<br>SATISFACTION<br>GUARANTEE</p>
</section>

<section class="flyer flyer--back">
  <svg class="shapes" viewBox="0 0 882 621">
    <defs>
      <linearGradient id="meetingTone" x1="0" y1="0" x2="1" y2="1">
        <stop offset="0" stop-color="#9a7b62"/><stop offset=".5" stop-color="#c9b7a6"/><stop offset="1" stop-color="#7d6a5a"/>
      </linearGradient>
    </defs>
    <polygon points="323,0 882,0 882,597 520,597" fill="var(--blue)"/>
    <polygon points="405,132 882,132 882,597 545,597" fill="var(--charcoal)"/>
    <polygon points="0,110 360,110 445,378 0,378" fill="url(#meetingTone)" role="img" aria-label="Photo of a team discussing around a meeting table"/>
    <polygon points="0,378 445,378 462,430 0,430" fill="var(--blue)"/>
    <line x1="370" y1="22" x2="405" y2="108" stroke="#fff" stroke-width="1.2"/>
    <circle cx="370" cy="22" r="4" fill="#fff"/>
    <line x1="405" y1="108" x2="876" y2="108" stroke="#fff" stroke-width="1.2"/>
    <polygon points="0,425 85,585 500,585 530,621 0,621" fill="var(--blue)"/>
    <g fill="#fff" stroke="#555" stroke-width="1.5">
      <circle cx="421" cy="164" r="21"/>
      <circle cx="446" cy="247" r="21"/>
      <circle cx="480" cy="331" r="21"/>
      <circle cx="508" cy="421" r="21"/>
      <circle cx="542" cy="511" r="21"/>
    </g>
    <g fill="none" stroke="#333" stroke-width="2" stroke-linecap="round" stroke-linejoin="round">
      <rect x="409" y="155" width="24" height="16" rx="1"/><line x1="416" y1="176" x2="426" y2="176"/>
      <path d="M441,237 q-5,10 3,20 l3,1 2,-3 -3,-4 -3,1 q-3,-5 0,-10 l3,1 2,-4 -3,-3 z"/>
      <rect x="469" y="323" width="22" height="15"/><polyline points="469,323 480,332 491,323"/>
      <circle cx="508" cy="421" r="12"/><ellipse cx="508" cy="421" rx="5" ry="12"/><line x1="496" y1="421" x2="520" y2="421"/><line x1="498" y1="415" x2="518" y2="415"/><line x1="498" y1="427" x2="518" y2="427"/>
      <path d="M552,511 a10,10 0 1 1 -4,-8" stroke-width="2.5"/><polyline points="545,499 549,504 543,507"/>
    </g>
    <g transform="translate(238,475)" fill="var(--blue-deep)">
      <path d="M2,10 Q12,0 22,10 L19,13 Q12,8 5,13 Z"/>
      <rect x="5" y="13" width="14" height="10" rx="2"/>
    </g>
  </svg>

  <div class="abs brand">
    <span class="brand__mark"></span>
    <div><div class="brand__name">BrantolHub</div><div class="brand__tag">Helping you work smarter</div></div>
  </div>

  <h2 class="abs headline headline--spaced">OTHER SERVICES</h2>

  <div class="abs service" style="left:465px;top:138px"><h3>Hosted Desktop</h3><p>Fully managed Cloud desktops, securely<br>available from anywhere and any device</p></div>
  <div class="abs service" style="left:490px;top:222px"><h3>Managed Telephony</h3><p>We provide Hosted VoIP telephony services,<br>fully managed with expert technical support</p></div>
  <div class="abs service" style="left:522px;top:308px"><h3>Desk Suite</h3><p>Fully managed Desk Suite migrations,<br>management services and support</p></div>
  <div class="abs service" style="left:551px;top:400px"><h3>Managed Internet</h3><p>Quick and reliable internet services<br>including broadband and leased lines</p></div>
  <div class="abs service" style="left:582px;top:490px"><h3>Disaster Recovery</h3><p>A range of backup and disaster<br>recovery solutions to keep your<br>business data safe and secure</p></div>

  <p class="abs caption">We provide fully accredited Managed IT Support,<br>&nbsp;Cloud and Communications solutions</p>

  <div class="abs cta" style="left:113px;top:468px">CALL US <span style="width:28px"></span><strong>03337159264</strong></div>
  <p class="abs address" style="left:121px;top:507px">BrantolHub Ltd, Unit 5, Ravensby Court,<br>&nbsp;Hertford, Hertfordshire, SG13 4PX</p>
  <p class="abs web">www.brantolhub.co.uk/gomanaged</p>
</section>

</body>
</html>
```